Commercial Office Fitout company needs a simple website

We need a website for our company Tallow Bridge (QLD) Pty Ltd. We are in the construction industry and we specialise in commercial office fitouts (partitions/glass/doors). Our company colours are black and silver. Please use our logo attached.
We only need an "about us" section, a "portfolio" section where we display some pictures of our work, and a "contact us" section. We would like our website to be simple, effective, professional and modern.

Industry/Entity Type

Construction

Number of Pages Required

1 page

```html
<!DOCTYPE html>
<html lang="en">
<head>
<meta charset="utf-8">
<title>Tallow Bridge (QLD) Pty Ltd — Commercial Office Fitouts</title>
<link rel="stylesheet" href="https://fonts.googleapis.com/css2?family=Questrial&display=swap">
<style>
  :root {
    --ink: #111111;
    --charcoal: #2e2e2e;
    --band: #323232;
    --slate: #5a5a5a;
    --silver: #c9c9c9;
    --mist: #e4e4e4;
    --paper: #ffffff;
    --muted: #777777;
    --field-line: #d6d6d6;
    --font: "Questrial", "Century Gothic", Arial, sans-serif;
  }
  * { box-sizing: border-box; margin: 0; padding: 0; }
  html, body { width: 1200px; height: 3020px; overflow: hidden; }
  body { position: relative; background: var(--paper); font-family: var(--font); color: var(--ink); }

  .abs { position: absolute; }
  .shape-layer { position: absolute; left: 0; top: 0; width: 1200px; height: 3020px; }

  /* brand mark: square + name */
  .brand { position: absolute; left: 0; width: 1200px; display: flex; flex-direction: column; align-items: center; }
  .brand-row { display: flex; align-items: center; gap: 12px; }
  .brand-square { width: 22px; height: 22px; background: currentColor; }
  .brand-name { font-size: 22px; letter-spacing: 3px; }
  .brand-sub { font-size: 12px; letter-spacing: 3px; margin-top: 4px; }

  /* hero */
  .hero-title { position: absolute; left: 0; width: 1200px; text-align: center; color: var(--paper); text-transform: uppercase; }
  .hero-title .line-1 { display: block; font-size: 33px; letter-spacing: 0.5px; }
  .hero-title .line-2 { display: block; font-size: 25px; margin-top: 6px; }

  .main-nav a { position: absolute; color: var(--paper); text-decoration: none; font-size: 15px; letter-spacing: 0.5px; text-transform: uppercase; }

  /* sections */
  .section-title { position: absolute; left: 0; width: 1200px; text-align: center; font-size: 24px; text-transform: uppercase; letter-spacing: 0.5px; }
  .about-copy { position: absolute; left: 250px; width: 700px; top: 1068px; text-align: center; font-size: 10.5px; line-height: 18px; color: var(--muted); }

  .tile { position: absolute; width: 264px; height: 184px; border: 4px solid var(--paper); box-shadow: 0 2px 6px rgba(0,0,0,.35); }
  .tile-overlay { position: absolute; inset: 0; background: rgba(40,40,40,.78); display: flex; flex-direction: column; align-items: center; justify-content: center; color: var(--paper); }
  .tile-overlay .tile-name { font-size: 15px; margin-top: 30px; }
  .tile-overlay .tile-note { font-size: 11px; color: var(--silver); margin-top: 8px; }
  .tile-overlay .tile-more { width: 22px; height: 22px; border-radius: 50%; background: var(--paper); color: var(--ink); font-size: 18px; line-height: 22px; text-align: center; margin-top: 8px; }

  .slider-track { position: absolute; left: 374px; top: 1914px; width: 446px; height: 14px; border-radius: 7px; background: var(--paper); }
  .slider-thumb { position: absolute; left: 4px; top: 4px; width: 44px; height: 6px; border-radius: 3px; background: var(--charcoal); }

  /* contact form */
  .field { position: absolute; border: 1px solid var(--field-line); font-size: 9px; color: #9a9a9a; padding: 16px 12px 0; text-transform: uppercase; letter-spacing: 0.5px; }
  .send-button { position: absolute; left: 526px; top: 2502px; width: 152px; height: 50px; background: var(--ink); color: var(--paper); font-size: 14px; text-align: center; line-height: 50px; letter-spacing: 1px; }

  /* footer */
  .social-list { position: absolute; top: 2858px; left: 0; width: 1200px; display: flex; justify-content: center; gap: 16px; }
  .social-dot { width: 14px; height: 14px; border-radius: 50%; background: var(--paper); }
  .footer-nav { position: absolute; top: 2904px; left: 0; width: 1200px; text-align: center; color: var(--paper); font-size: 12px; letter-spacing: 0.5px; }
  .footer-nav span.sep { margin: 0 14px; }
  .copyright { position: absolute; top: 2944px; left: 0; width: 1200px; text-align: center; color: var(--silver); font-size: 11px; letter-spacing: 0.4px; }
</style>
</head>
<body>

<svg class="shape-layer" viewBox="0 0 1200 3020" aria-hidden="true">
  <defs>
    <linearGradient id="heroTone" x1="0" y1="0" x2="0" y2="1">
      <stop offset="0" stop-color="#6a6a6a"/>
      <stop offset="0.5" stop-color="#3c3c3c"/>
      <stop offset="1" stop-color="#555555"/>
    </linearGradient>
    <linearGradient id="officeTone" x1="0" y1="0" x2="1" y2="1">
      <stop offset="0" stop-color="#f2f2f2"/>
      <stop offset="0.5" stop-color="#b9c1c4"/>
      <stop offset="1" stop-color="#8e9699"/>
    </linearGradient>
    <linearGradient id="cityTone" x1="0" y1="0" x2="0" y2="1">
      <stop offset="0" stop-color="#8c8c8c"/>
      <stop offset="0.6" stop-color="#5e5e5e"/>
      <stop offset="1" stop-color="#3e3e3e"/>
    </linearGradient>
  </defs>
</svg>

<!-- Hero -->
<svg class="abs" style="left:0;top:0" width="1200" height="530" viewBox="0 0 1200 530">
  <rect width="1200" height="470" fill="url(#heroTone)" role="img" aria-label="Black and white aerial photograph of a city skyline at dusk"/>
  <polygon points="0,430 600,400 1200,420 1200,470 600,522 0,480" fill="var(--band)"/>
</svg>
<svg class="abs" style="left:0;top:0;width:1200px;height:530px" viewBox="0 0 1200 530" aria-hidden="true">
  <defs>
    <linearGradient id="heroTone" x1="0" y1="0" x2="0" y2="1">
      <stop offset="0" stop-color="#6a6a6a"/><stop offset="0.5" stop-color="#3c3c3c"/><stop offset="1" stop-color="#555555"/>
    </linearGradient>
  </defs>
  <rect width="1200" height="440" fill="url(#heroTone)" role="img" aria-label="Black and white aerial photograph of a city skyline at dusk"/>
  <polygon points="0,420 600,400 1200,410 1200,470 600,522 0,478" fill="#323232"/>
</svg>

<div class="brand" style="top:150px;color:var(--paper)">
  <div class="brand-row"><span class="brand-square"></span><span class="brand-name">TALLOW BRIDGE</span></div>
</div>

<h1 class="hero-title" style="top:262px">
  <span class="line-1">We are in the construction industry &amp;</span>
  <span class="line-2">We specialise in commercial office fitouts</span>
</h1>

<nav class="main-nav">
  <a style="left:296px;top:462px">Home</a>
  <a style="left:398px;top:472px">About Us</a>
  <a style="left:670px;top:476px">Portfolio</a>
  <a style="left:806px;top:462px">Contact Us</a>
</nav>

<div class="brand" style="top:462px;color:var(--paper)">
  <span class="brand-square" style="width:34px;height:34px"></span>
</div>
<div class="brand" style="top:526px;color:var(--ink)">
  <span class="brand-name" style="font-size:20px">TALLOW BRIDGE</span>
  <span class="brand-sub" style="font-size:10px;margin-top:2px">(QLD) PTY LTD</span>
</div>

<!-- About -->
<svg class="abs" style="left:244px;top:634px" width="712" height="358" viewBox="0 0 712 358">
  <defs>
    <linearGradient id="officeFill" x1="0" y1="0" x2="1" y2="1">
      <stop offset="0" stop-color="#f4f4f4"/><stop offset="0.45" stop-color="#c4cbce"/><stop offset="1" stop-color="#8f979a"/>
    </linearGradient>
  </defs>
  <polygon points="6,34 356,4 706,34 706,324 356,354 6,324" fill="#e8e8e8"/>
  <polygon points="14,40 356,12 698,40 698,318 356,346 14,318" fill="url(#officeFill)" role="img" aria-label="Bright open-plan office with glass partitions and a yellow lounge chair"/>
</svg>

<h2 class="section-title" style="top:1010px">About Us</h2>
<p class="about-copy">
  Tallow Bridge delivers commercial office fitouts across Queensland, from glass partitions and framed doors to complete floor refurbishments. Our team plans each project around how your staff work, then builds it on time with minimal disruption to your business. We manage trades, certification and handover so you can focus on moving in. Every fitout is finished to a clean, modern standard that is built to last, with clear pricing and direct contact throughout.
</p>

<!-- Portfolio -->
<svg class="abs" style="left:0;top:1196px" width="1200" height="820" viewBox="0 0 1200 820">
  <defs>
    <linearGradient id="cityFill" x1="0" y1="0" x2="0" y2="1">
      <stop offset="0" stop-color="#8a8a8a"/><stop offset="0.6" stop-color="#5c5c5c"/><stop offset="1" stop-color="#404040"/>
    </linearGradient>
  </defs>
  <polygon points="0,114 600,0 1200,104 1200,690 600,814 0,688" fill="url(#cityFill)" role="img" aria-label="Black and white photograph of city towers and a bridge"/>
</svg>

<div class="brand" style="top:1308px;color:var(--paper)">
  <span class="brand-square" style="width:30px;height:30px"></span>
</div>
<h2 class="section-title" style="top:1372px;color:var(--paper)">Portfolio</h2>

<div class="tile" style="left:176px;top:1468px;background:linear-gradient(135deg,#9a9a9a,#4e4e4e)" role="img" aria-label="Glass-walled meeting room">
  <div class="tile-overlay">
    <span class="tile-name">Tallow Bridge</span>
    <span class="tile-note">At vero eos et accusamus et iusto odio</span>
    <span class="tile-more">+</span>
  </div>
</div>
<div class="tile" style="left:464px;top:1468px;background:linear-gradient(135deg,#d9cfbf,#9c8e78)" role="img" aria-label="Office floor with workstation partitions"></div>
<div class="tile" style="left:754px;top:1468px;background:linear-gradient(135deg,#cfd6cf,#7f8a80)" role="img" aria-label="Corridor lined with frosted glass doors"></div>
<div class="tile" style="left:176px;top:1676px;background:linear-gradient(135deg,#e6e6e6,#6c6c6c)" role="img" aria-label="Boardroom behind full-height glazing"></div>
<div class="tile" style="left:464px;top:1676px;background:linear-gradient(135deg,#ededed,#9aa09c)" role="img" aria-label="Glass sliding doors with planter boxes"></div>
<div class="tile" style="left:754px;top:1676px;background:linear-gradient(135deg,#fbf7ef,#d8d1c2)" role="img" aria-label="Sunlit office with white glass partitions"></div>

<div class="slider-track"><span class="slider-thumb"></span></div>

<!-- Contact -->
<div class="brand" style="top:2074px;color:var(--ink)">
  <span class="brand-square" style="width:30px;height:30px"></span>
</div>
<h2 class="section-title" style="top:2144px">Contact Us</h2>

<form>
  <div class="field" style="left:246px;top:2216px;width:340px;height:44px">Name</div>
  <div class="field" style="left:608px;top:2216px;width:338px;height:44px">E-mail</div>
  <div class="field" style="left:246px;top:2280px;width:340px;height:44px">Phone</div>
  <div class="field" style="left:608px;top:2280px;width:338px;height:44px">Location</div>
  <div class="field" style="left:246px;top:2352px;width:700px;height:120px;padding-top:14px">Message</div>
  <div class="send-button">SEND</div>
</form>

<!-- Footer -->
<svg class="abs" style="left:0;top:2620px" width="1200" height="400" viewBox="0 0 1200 400" aria-hidden="true">
  <polygon points="0,72 600,6 1200,72 1200,400 0,400" fill="#2e2e2e"/>
</svg>

<footer>
  <div class="brand" style="top:2734px;color:var(--paper)">
    <span class="brand-square" style="width:30px;height:30px"></span>
    <span class="brand-name" style="font-size:20px;margin-top:12px">TALLOW BRIDGE</span>
    <span class="brand-sub" style="font-size:10px;margin-top:2px">(QLD) PTY LTD</span>
  </div>
  <div class="social-list">
    <span class="social-dot"></span><span class="social-dot"></span><span class="social-dot"></span>
    <span class="social-dot"></span><span class="social-dot"></span><span class="social-dot"></span>
  </div>
  <div class="footer-nav">HOME<span class="sep">|</span>ABOUT US<span class="sep">|</span>PORTFOLIO<span class="sep">|</span>CONTACT US</div>
  <div class="copyright">© 2016 COMPANY NAME &nbsp;|&nbsp; ALL RIGHTS RESERVED</div>
</footer>

</body>
</html>
```